Industry and Trade -may go complete production

Industrial and Corporate Clothing ecom and showcase web site
see supplier ref sites:
www.grellonworkgear.example.com.au
www.mickysprocket.example.com/,
www.Koradyn.example.com.au
Our logo is a roundal shaped gear cog with an elephant inside it.
Main Objective

Get people to contact us for industrial and corporate wear
order online or contact us for more details on products

Information in seconday pages inmportant and ISO standards etc.
Primary Points:

Must show that we are strong and solid.
Visual imagery is important.
We have many web sites in line and this is a start, see zanterfreight.example.com.au for one of ours.

We need a layout for the home page and internal pages. It's an ecomm retail site! Must sell the products AND our company.

Internal pages would be product description pages.

Each page must present an opportunity for them to contact us.
Updates

http://shop.qvx.example.com/siege-of-marrowfen-a-stonehelm-table-game/detail.php?p=481736&v=qvx_series_crown-of-ashes_games#tabs

has very good features 

Reason: Not Enough Responses. This will open up to a designer doing continuous designs for our company. We had lost our last in house designer and need a new innovative person to create genius.

Hi

This tender has been extended due to non response. 
This is our first look at the system as we had designers inder contract who have now left. There are may web sites etc to be done and this is more of a interview.

It is well worth responding. There are already 6 other projects in the pipline. But we want the best .
Barney ter Haust
Group COO Meridale Carriage Pty Ltd
Sydney Australia.

Target Market(s)

TARGET MARKET:
Tradesmen and Corporations and Government agencies
again see the above web sites they address the same markets
especially grellon.example.com.au

Industry/Entity Type

Industrial

Requirements
Must have
• Strength of company
supply and quality are important
ease of use, grellon.example.com.au can be used for good visual expression.
Nice to have
• extreme images and ease of use in navigation and contact.
look at imagery on grellon web site grellon.example.com.au
font useage: see http://money.quorvix.example.com.au/newsbusiness/wire/5193027/dalvane-signs-11b-grid-agreement for font size usage. clear clean to the point.
Should not have
• kitch

```html
<!DOCTYPE html>
<html lang="en">
<head>
<meta charset="utf-8">
<title>Forgeline Supply</title>
<link href="https://fonts.googleapis.com/css2?family=Arimo:wght@400;700&family=Delius&display=swap" rel="stylesheet">
<style>
:root{
  --bg-top:#1b2133;
  --bg-band:#000;
  --bg-low:#262626;
  --navy:#17245e;
  --navy-light:#2a3d8f;
  --panel:#1e1e1e;
  --text:#fff;
  --muted:#a9a9a9;
  --link:#3e5fd6;
  --rule:#555;
}
*{box-sizing:border-box;margin:0;padding:0}
html,body{width:1109px;height:1200px;overflow:hidden;background:var(--bg-low)}
body{font-family:"Arimo",Arial,sans-serif;color:var(--text)}
.page{position:absolute;left:0;top:0;width:1200px;height:1299px;transform:scale(.92417);transform-origin:0 0;
  background:linear-gradient(180deg,var(--bg-top) 0,#151a28 300px,#0a0c12 365px,var(--bg-band) 370px,#070707 520px,#1a1a1a 640px,var(--bg-low) 900px,var(--bg-low) 100%)}
.abs{position:absolute}
.column-glow{left:100px;top:0;width:950px;height:380px;background:linear-gradient(90deg,rgba(255,255,255,0),rgba(120,140,200,.06) 50%,rgba(255,255,255,0))}
.brand-badge{left:105px;top:22px;width:302px;height:110px;background:linear-gradient(160deg,#22306f,var(--navy) 60%,#0d153b);transform:rotate(-3deg);border-radius:3px;box-shadow:0 0 18px rgba(150,170,255,.35)}
.brand{left:128px;top:42px;height:70px;display:flex;align-items:center;gap:14px}
.brand-dot{width:60px;height:60px;border-radius:50%;background:#2c3f8c;flex:none}
.brand-name{font-family:"Arimo",sans-serif;font-weight:700;font-size:27px;line-height:30px;color:#fff;text-transform:uppercase}
.contact-box{left:858px;top:10px;width:188px;height:40px;background:var(--navy);border-radius:5px;box-shadow:0 0 10px rgba(140,160,255,.35);font-size:11px;line-height:17px;text-align:right;padding:4px 20px 0 0}
.nav{left:400px;top:58px;width:650px;height:42px;background:#0f0f10;display:flex;justify-content:flex-end;padding-right:36px}
.nav a{color:#fff;text-decoration:none;font-variant:small-caps;font-size:14px;letter-spacing:.6px;line-height:40px;margin-left:21px}
.hero{left:141px;top:120px;width:906px;height:277px;border-radius:5px;background:linear-gradient(100deg,#e9e9e9 0,#d8d8d4 20%,#f0c21a 38%,#f5d230 50%,#e4b412 58%,#c9c6bc 70%,#8da4c2 86%,#b8c6d8 100%)}
.hero-caption{left:157px;top:327px;width:353px;height:43px;border-radius:6px;background:linear-gradient(180deg,#c4c4c4,#7b7b7b);box-shadow:0 3px 6px rgba(0,0,0,.5);font-size:23px;line-height:43px;text-align:center;color:#fff;letter-spacing:.8px}
.hero-reflection{left:141px;top:400px;width:906px;height:50px;background:linear-gradient(180deg,rgba(140,130,90,.35),rgba(0,0,0,0))}
.intro-title{left:142px;top:464px;font-size:18px;font-weight:400}
.intro-text{left:146px;top:500px;width:592px;font-size:11px;line-height:16px;letter-spacing:.35px;color:var(--muted)}
.vrule{width:1px;background:linear-gradient(180deg,transparent,#999,transparent)}
.promo{left:811px;top:466px;width:236px;height:124px;border:1px solid #777;border-radius:5px;background:linear-gradient(160deg,#161a25 30%,#4a5a9a 60%,#0c0f18 80%);text-align:center}
.promo-title{font-family:"Delius",cursive;font-size:32px;margin-top:8px}
.promo-sub{font-family:"Delius",cursive;font-size:15px;margin-top:4px}
.btn{display:inline-block;background:var(--navy);border:1px solid #3c4fa0;border-radius:4px;color:#fff;font-size:11px;text-align:center}
.promo .btn{width:85px;height:26px;line-height:24px;margin-top:8px}
.products{left:140px;top:614px;width:906px;height:340px;border-radius:4px;background:linear-gradient(180deg,var(--panel),#232323 75%,var(--bg-low))}
.strip{left:158px;top:634px;width:870px;height:178px;background:#000}
.shot{border:1px solid #777}
.shot-steel{left:215px;top:646px;width:215px;height:136px;background:linear-gradient(120deg,#3a1a10,#a03d10 40%,#f4a020 55%,#5a2810)}
.shot-flame{left:475px;top:646px;width:237px;height:135px;background:radial-gradient(ellipse at 50% 45%,#fff4c8,#f7a413 35%,#8a2c06 75%,#2b0d04)}
.shot-plant{left:757px;top:646px;width:214px;height:136px;background:linear-gradient(180deg,#6b5a24,#3e3514 45%,#e3b630 75%,#352a0c)}
.card{width:230px}
.card h3{font-weight:400;font-size:18px;letter-spacing:.3px}
.card p{width:214px;font-size:11px;line-height:16px;letter-spacing:.35px;color:var(--muted);margin-top:6px}
.card a{display:block;margin-top:9px;font-size:11px;letter-spacing:.3px;color:var(--link);text-decoration:none}
.info h4{font-weight:400;font-size:14px;display:flex;align-items:center;gap:8px}
.bullet{width:12px;height:12px;border-radius:50%;background:radial-gradient(circle at 40% 40%,#6b7fd0,#101a40)}
.info p{font-size:11px;line-height:13px;color:var(--muted)}
.info .date{font-style:italic;color:#fff;font-size:11px}
.info .more{font-style:italic;color:var(--link);font-size:10px;text-align:right;display:block}
.arrow-list li{list-style:none;display:flex;gap:6px;font-size:11px;line-height:13px;color:var(--muted);margin-bottom:11px}
.footer{left:103px;top:1196px;width:977px;height:89px;background:linear-gradient(180deg,#000,#141414)}
.footer-col{font-size:11px;line-height:16px}
.footer-links{display:flex;font-size:11px}
.footer-links span{padding:0 11px;border-left:1px solid #fff}
.footer-links span:first-child{border-left:0}
.footer-links.legal span{color:var(--link);border-color:#666}
</style>
</head>
<body>
<div class="page">
  <div class="abs column-glow"></div>

  <div class="abs brand-badge"></div>
  <div class="abs brand"><span class="brand-dot"></span><span class="brand-name">Forgeline<br>Supply</span></div>
  <div class="abs contact-box">Call Us:&nbsp; 555-555-5555<br>Email: domain@address.com</div>
  <nav class="abs nav"><a>Home</a><a>About Us</a><a>Services</a><a>Products</a><a>FAQs</a><a>Materials</a><a>Contact</a></nav>

  <div class="abs hero" role="img" aria-label="Worker in denim and gloves holding a yellow hard hat"></div>
  <div class="abs hero-caption">CONSTRUCTION INDUSTRY</div>
  <div class="abs hero-reflection"></div>

  <h1 class="abs intro-title">Leading Manufacturer Of Quality Safety Clothing &amp; Corporate Wear</h1>
  <p class="abs intro-text">Aliquam erat volutpat. Cras sed ligula mi, quis gravida nunc. Pellentesque urna eros, porta sed semper sed, consectetur non libero. Vivamus odio dui, convallis sit amet porta eget, sollicitudin eget mi. Donec quis orci at leo euismod vulputate quis a augue. Etiam quam turpis, semper dapibus imperdiet eu, vehicula ut odio. Praesent vitae consequat sem.</p>
  <div class="abs vrule" style="left:784px;top:462px;height:128px"></div>
  <div class="abs promo">
    <div class="promo-title">Top Products</div>
    <div class="promo-sub">Lorem Ipsum Dolor</div>
    <span class="btn">Click Here</span>
  </div>

  <div class="abs products"></div>
  <div class="abs strip"></div>
  <svg class="abs" style="left:172px;top:642px" width="24" height="140" viewBox="0 0 24 140"><path d="M20 2 L4 70 L20 138 L14 70 Z" fill="#3a3f30" stroke="#9aa08a" stroke-width="1"/></svg>
  <svg class="abs" style="left:992px;top:642px" width="24" height="140" viewBox="0 0 24 140"><path d="M4 2 L20 70 L4 138 L10 70 Z" fill="#3a3f30" stroke="#9aa08a" stroke-width="1"/></svg>
  <div class="abs shot shot-steel" role="img" aria-label="Sparks flying from steel cutting"></div>
  <div class="abs shot shot-flame" role="img" aria-label="Firefighter facing a large flame burst"></div>
  <div class="abs shot shot-plant" role="img" aria-label="Industrial plant lit up at night"></div>

  <div class="abs card" style="left:220px;top:822px"><h3>Steel Industry</h3><p>Cras sollicitudin mi placerat eros moles tie non gravida mi fermentum. Morbi plac erat fermentum justo, nec facilisis velit pharetra ut.</p><a>Phasellus laoreet fringilla lorem at &gt;&gt;</a></div>
  <div class="abs card" style="left:480px;top:822px"><h3>Flame Retardant</h3><p>Cras sollicitudin mi placerat eros moles tie non gravida mi fermentum. Morbi plac erat fermentum justo, nec facilisis velit pharetra ut.</p><a>Phasellus laoreet fringilla lorem at &gt;&gt;</a></div>
  <div class="abs card" style="left:757px;top:822px"><h3>Electrical Industry</h3><p>Cras sollicitudin mi placerat eros moles tie non gravida mi fermentum. Morbi plac erat fermentum justo, nec facilisis velit pharetra ut.</p><a>Phasellus laoreet fringilla lorem at &gt;&gt;</a></div>

  <section class="abs info" style="left:166px;top:991px;width:245px">
    <h4><span class="bullet"></span>Lorem Ipsum Dolor</h4>
    <p style="margin-top:15px">Aliquam erat volutpat. Cras sed ligula mi, quis gravida nunc. Pellentesque urna eros, porta sed semper sed, consectetur non libero. Vivam us odio dui, convallis sit amet porta eget, solli citudin eget mi. Donec quis orci at leo euismod vulputate quis a augue.</p>
    <span class="btn" style="position:absolute;left:156px;top:119px;width:86px;height:28px;line-height:26px">Click Here</span>
  </section>
  <div class="abs vrule" style="left:443px;top:998px;height:125px"></div>
  <section class="abs info" style="left:468px;top:991px;width:255px">
    <h4><span class="bullet"></span>Lorem Ipsum Dolor</h4>
    <ul class="arrow-list" style="margin-top:15px">
      <li><span style="color:#fff">&#10148;</span><span>Aliquam erat volutpat. Cras sed ligula mi, quis gravida nunc. Pellentesque urna.</span></li>
      <li><span style="color:#fff">&#10148;</span><span>Aliquam erat volutpat. Cras sed ligula mi, quis gravida nunc. Pellentesque urna.</span></li>
      <li><span style="color:#fff">&#10148;</span><span>Aliquam erat volutpat. Cras sed ligula mi, quis gravida nunc. Pellentesque urna.</span></li>
    </ul>
  </section>
  <div class="abs vrule" style="left:739px;top:998px;height:125px"></div>
  <section class="abs info" style="left:768px;top:991px;width:248px">
    <h4><span class="bullet"></span>Lorem Ipsum Dolor</h4>
    <div style="padding-left:4px">
      <div class="date" style="margin-top:15px">MM/DD/YY</div>
      <p>Aliquam erat volutpat. Cras sed ligula mi, quisg vida nunc. Pellentesque urna eros, porta seds sed, consectetur non libero.</p>
      <span class="more">read more...</span>
      <div class="date" style="margin-top:8px">MM/DD/YY</div>
      <p>Aliquam erat volutpat. Cras sed ligula mi, quisg vida nunc..</p>
      <span class="more">read more...</span>
    </div>
  </section>

  <footer class="abs footer">
    <div class="abs footer-col" style="left:66px;top:11px">FORGELINE SUPPLY PVT LTD.<div style="margin-top:2px;line-height:14px">No., Street No.<br>City and Country</div></div>
    <div class="abs footer-col" style="left:331px;top:11px;line-height:17px">Call Us: 555-555-5555<br>Fax: 555-555-5555<br>Email: domain@address.com</div>
    <div class="abs footer-links" style="left:668px;top:12px"><span>Home</span><span>About Us</span><span>Products</span><span>Services</span></div>
    <div class="abs footer-links legal" style="left:710px;top:43px"><span>Privacy Policy</span><span>Disclaimer</span></div>
  </footer>
</div>
</body>
</html>
```